RWP Tax Services
RWP Tax Services -
Creative Brief
Professional
Dan Feltwicke
President
2847 Harbor Street, Suite 210 San Jose, CA 95128
dan@rwptaxdemo.com
www.rwptaxdemo.com
We want the card to look and feel like it is a combination of real estate business card and CPA business card. Tax professional (CPA office) with photo (real estate business) of president.

```html
<!DOCTYPE html>
<html lang="en">
<head>
<meta charset="utf-8">
<title>RWP Tax Services – Business Card</title>
<link rel="stylesheet" href="https://fonts.googleapis.com/css2?family=Arimo:wght@400;700&display=swap">
<style>
  :root {
    --page-bg: #f4f4f4;
    --card-light: #ffffff;
    --card-sky: #a9d3ef;
    --brand-blue: #2a64ad;
    --deep-blue: #1d5aa3;
    --accent-orange: #f07c1e;
    --text-white: #ffffff;
    --photo-top: #c9dced;
    --photo-bottom: #8fb1d2;
  }
  * { box-sizing: border-box; margin: 0; padding: 0; }
  html, body {
    width: 1200px; height: 1030px; overflow: hidden;
    background: var(--page-bg);
    font-family: "Arimo", Arial, sans-serif;
  }
  .business-card {
    position: absolute; left: 75px; top: 215px;
    width: 1050px; height: 600px;
    border-radius: 28px; overflow: hidden;
    background: radial-gradient(ellipse at 48% 20%, var(--card-light) 0%, #e3f1fb 35%, var(--card-sky) 100%);
  }
  .card-shapes { position: absolute; inset: 0; }
  .brand-name {
    position: absolute; left: 95px; top: 92px;
    display: flex; align-items: center; gap: 16px;
    font-size: 46px; font-weight: 400; color: var(--brand-blue);
    letter-spacing: 0.5px;
  }
  .brand-square { width: 26px; height: 26px; background: var(--accent-orange); }
  .president-photo {
    position: absolute; left: 585px; top: 70px;
    width: 130px; height: 160px;
    border-radius: 8px;
    border: 4px solid var(--card-light);
    background: linear-gradient(180deg, var(--photo-top), var(--photo-bottom));
    box-shadow: 0 2px 8px rgba(29, 90, 163, 0.25);
  }
  .person-name {
    position: absolute; left: 95px; top: 335px;
    font-size: 34px; font-weight: 400; color: var(--brand-blue);
  }
  .person-title {
    position: absolute; left: 178px; top: 377px;
    font-size: 17px; font-weight: 400; color: var(--brand-blue);
  }
  .office-address {
    position: absolute; right: 505px; top: 490px;
    text-align: right; font-size: 18px; font-weight: 700; font-style: normal;
    line-height: 28px; color: var(--text-white);
  }
  .contact-list {
    position: absolute; left: 560px; top: 443px;
    font-size: 18px; font-weight: 700; line-height: 27px;
    color: var(--text-white);
  }
  .contact-row { display: flex; }
  .contact-label { width: 100px; }
</style>
</head>
<body>
  <main class="business-card">
    <svg class="card-shapes" width="1050" height="600" viewBox="0 0 1050 600" aria-hidden="true">
      <path d="M0,445 C320,445 560,405 700,285 C820,180 880,45 1050,35 L1050,600 L0,600 Z" fill="var(--deep-blue)"/>
      <path d="M0,432 C320,434 555,392 690,272 C808,166 872,30 1010,20" fill="none" stroke="var(--accent-orange)" stroke-width="7" stroke-linecap="round"/>
    </svg>

    <div class="brand-name"><span>RWP Tax Services</span><span class="brand-square"></span></div>

    <div class="president-photo" role="img" aria-label="Portrait photo of Dan Feltwicke, President"></div>

    <h1 class="person-name">Dan Feltwicke</h1>
    <p class="person-title">President</p>

    <address class="office-address">
      2847 Harbor Street, Suite 210<br>San Jose, CA 95128
    </address>

    <div class="contact-list">
      <div class="contact-row"><span class="contact-label">Toll free</span><span>(877) 555-0142</span></div>
      <div class="contact-row"><span class="contact-label">Phone</span><span>(408) 555-0163</span></div>
      <div class="contact-row"><span class="contact-label">Fax</span><span>(408) 555-0179</span></div>
      <div class="contact-row"><span class="contact-label">Email</span><span>dan@rwptaxdemo.com</span></div>
      <div class="contact-row"><span>www.rwptaxdemo.com</span></div>
    </div>
  </main>
</body>
</html>
```